Law Firm Investment Immigration Brochure

I'm looking to have a brochure designed for my law firm. The brochure will be about investment immigration and will be designed to attract potential immigrations.
As this program is geared towards wealthier clients, I will need the winning brochure design to be classy.
The overall theme of my brochure should be to look simple, elegant, smart and professional.
I would like the delivery of the brochure in high-res PSD and AI formats in CS1 and CS3, which can be resized later to any resolution possible (print ready included). I will then own the rights to the content once the work has been paid for. I will need multiple formats - .psd (CS1 and CS3), .ai (CS1 and CS3), .jpg, and .gif.
I have included a copy of my logo design so please design the brochure accordingly.
The name of my law firm is "Law Offices of Marcel Dovrane".
Thanks in advance.
Updates
Even though my brochure is 1 page, I will be folding it twice, so that it looks like an "N". The side that clients will see first will act as the cover page. Therefore, on it, I would like you to include my logo design and then my office address (which I will supply to you later). My cover page would take up the right 1/3 of this design you will submit. Therefore, please submit a design which would take up the left 2/3 of the page, and then design a cover page that will take up the right 1/3 of the page. Just so you know, my brochure will be 2-sided, so please show me what both sides will look like. The back side of the brochure will have all written content, and no cover page. Therefore, please design the whole back side of the brochure as one, instead of the front side, which is split 2/3 and 1/3. Thank you in advance, Marc

```html
<!DOCTYPE html>
<html lang="en">
<head>
<meta charset="utf-8">
<title>Law Offices of Marcel Dovrane — Investment Immigration Brochure</title>
<link rel="stylesheet" href="https://fonts.googleapis.com/css2?family=Cinzel:wght@600;700&family=Barlow:wght@400;500;600&display=swap">
<style>
  :root {
    --royal-blue: #1c1f97;
    --slate: #3d4849;
    --quote-grey: #9a9e9e;
    --pill-blue: #2326a8;
    --ink-navy: #23264f;
    --white: #ffffff;
    --line: rgba(255, 255, 255, 0.55);
    --heading-font: "Cinzel", serif;
    --body-font: "Barlow", sans-serif;
  }
  * { margin: 0; padding: 0; box-sizing: border-box; }
  html, body {
    width: 1200px; height: 531px; overflow: hidden;
    background: #ffffff;
  }
  .brochure {
    position: absolute; left: 24px; top: 16px;
    width: 1152px; height: 498px;
    box-shadow: 3px 4px 8px rgba(0, 0, 0, 0.35);
    overflow: hidden;
    font-family: var(--body-font);
    color: var(--white);
  }
  .backdrop { position: absolute; inset: 0; }
  .section-title {
    position: absolute;
    font-family: var(--heading-font);
    font-weight: 700;
    font-size: 14px;
    letter-spacing: 1.2px;
    line-height: 1.05;
    color: var(--white);
    white-space: nowrap;
  }
  .copy {
    position: absolute;
    font-size: 6.2px;
    line-height: 1.45;
    font-weight: 500;
  }
  .copy p { margin-bottom: 5px; }
  .copy .subhead {
    text-align: center; font-weight: 600; letter-spacing: 0.5px;
    text-transform: uppercase; margin-bottom: 4px;
  }
  .testimonial {
    position: absolute;
    background: var(--quote-grey);
    border-radius: 2px 14px 2px 14px;
    padding: 8px 7px 7px 8px;
    font-size: 6px; line-height: 1.4; font-weight: 500;
  }
  .testimonial .attribution { text-align: right; margin-top: 4px; }

  .why-title { left: 40px; top: 20px; }
  .why-copy { left: 24px; top: 38px; width: 142px; }
  .quote-top { left: 228px; top: 126px; width: 90px; }

  .team-title { left: 596px; top: 20px; }
  .team-copy { left: 550px; top: 38px; width: 172px; }

  .contact-title { left: 455px; top: 232px; width: 244px; text-align: center; }
  .contact-copy {
    left: 455px; top: 255px; width: 244px; text-align: center;
    font-size: 6.6px; line-height: 1.6;
  }
  .contact-copy .intro { margin-bottom: 8px; }
  .contact-copy address { font-style: normal; }

  .joining-title { left: 160px; top: 272px; width: 130px; text-align: center; }
  .joining-copy { left: 158px; top: 304px; width: 130px; }
  .quote-bottom { left: 24px; top: 327px; width: 92px; }

  .firm-name {
    position: absolute; left: 938px; top: 233px; width: 210px;
    font-family: var(--body-font); font-weight: 500;
    font-size: 13px; line-height: 1.3; letter-spacing: 1.6px;
    color: var(--ink-navy); text-transform: uppercase; text-align: center;
  }
  .services { position: absolute; left: 993px; top: 362px; list-style: none; }
  .services li {
    width: 159px; height: 13px; margin-bottom: 5.5px;
    background: var(--pill-blue);
    border: 1px solid var(--white); border-right: none;
    border-radius: 8px 0 0 8px;
    font-size: 6px; font-weight: 600; letter-spacing: 1px;
    text-transform: uppercase; line-height: 11px; padding-left: 12px;
    white-space: nowrap;
  }
</style>
</head>
<body>
<main class="brochure">
  <svg class="backdrop" width="1152" height="498" viewBox="0 0 1152 498" xmlns="http://www.w3.org/2000/svg">
    <defs>
      <linearGradient id="tone-team-wide" x1="0" y1="0" x2="1" y2="0">
        <stop offset="0" stop-color="#e9e4df"/>
        <stop offset="0.5" stop-color="#c9b2a2"/>
        <stop offset="1" stop-color="#f1ece8"/>
      </linearGradient>
      <radialGradient id="tone-dark-suits" cx="0.5" cy="0.4" r="0.6">
        <stop offset="0" stop-color="#7e8587"/>
        <stop offset="1" stop-color="#2c3134"/>
      </radialGradient>
      <radialGradient id="tone-office" cx="0.5" cy="0.5" r="0.6">
        <stop offset="0" stop-color="#d9e3e6"/>
        <stop offset="1" stop-color="#7f9aa3"/>
      </radialGradient>
      <radialGradient id="tone-skin-light" cx="0.5" cy="0.5" r="0.6">
        <stop offset="0" stop-color="#e8cbb6"/>
        <stop offset="1" stop-color="#b8a59b"/>
      </radialGradient>
      <radialGradient id="tone-globe-blue" cx="0.5" cy="0.5" r="0.6">
        <stop offset="0" stop-color="#8fb8da"/>
        <stop offset="1" stop-color="#2f5d8f"/>
      </radialGradient>
      <linearGradient id="tone-building" x1="0" y1="0" x2="0" y2="1">
        <stop offset="0" stop-color="#b7d2e6"/>
        <stop offset="1" stop-color="#7e8a92"/>
      </linearGradient>
      <radialGradient id="tone-headscarf" cx="0.45" cy="0.5" r="0.6">
        <stop offset="0" stop-color="#d8b9a6"/>
        <stop offset="1" stop-color="#4b3f3b"/>
      </radialGradient>
    </defs>

    <rect class="band-top" x="0" y="0" width="1152" height="227" fill="var(--royal-blue)"/>
    <rect class="band-bottom" x="0" y="227" width="1152" height="271" fill="var(--slate)"/>

    <path role="img" aria-label="Photo: smiling business team applauding"
          d="M800 200 C820 100 910 22 1060 0 L1152 0 L1152 200 Z" fill="url(#tone-team-wide)"/>
    <rect class="logo-strip" x="865" y="219" width="287" height="59" fill="var(--white)"/>

    <g fill="none" stroke="var(--line)" stroke-width="1">
      <path d="M0 312 C60 296 90 280 108 270"/>
      <path d="M138 270 C220 250 290 270 340 300 C460 360 600 330 672 304 C780 270 850 232 896 248"/>
      <path d="M0 96 C70 92 140 86 170 82"/>
      <path d="M250 82 C330 72 400 78 450 84"/>
      <path d="M520 92 C570 110 600 140 612 148 C720 130 800 90 840 60"/>
      <path d="M172 0 C160 60 165 120 180 160"/>
      <path d="M330 346 C380 410 470 432 529 430"/>
      <path d="M629 428 C720 430 800 420 830 392"/>
      <path d="M480 160 C478 250 520 330 560 380"/>
      <path d="M380 498 C470 430 530 400 560 390"/>
      <path d="M740 296 C850 230 980 160 1152 118"/>
      <path d="M1152 336 C990 328 945 360 950 400 C955 445 1050 472 1152 472"/>
      <path d="M0 470 C40 462 60 455 80 445"/>
    </g>

    <g stroke="var(--white)" stroke-width="2">
      <circle role="img" aria-label="Photo: colleagues in a meeting" cx="210" cy="80" r="40" fill="url(#tone-office)"/>
      <circle role="img" aria-label="Photo: team of business professionals" cx="450" cy="82" r="70" fill="url(#tone-dark-suits)"/>
      <circle role="img" aria-label="Photo: consultant with headset" cx="640" cy="150" r="27" fill="url(#tone-skin-light)"/>
      <circle role="img" aria-label="Photo: hand signing a document" cx="108" cy="272" r="30" fill="url(#tone-skin-light)"/>
      <circle role="img" aria-label="Photo: handshake over a globe" cx="340" cy="300" r="46" fill="url(#tone-globe-blue)"/>
      <circle role="img" aria-label="Photo: receptionist with headset" cx="710" cy="304" r="38" fill="url(#tone-skin-light)"/>
      <circle role="img" aria-label="Photo: modern office building" cx="579" cy="430" r="50" fill="url(#tone-building)"/>
      <circle role="img" aria-label="Photo: clients from the Middle East" cx="859" cy="372" r="52" fill="url(#tone-headscarf)"/>
      <circle role="img" aria-label="Photo: business people talking" cx="896" cy="248" r="27" fill="url(#tone-office)"/>
    </g>
  </svg>

  <h2 class="section-title why-title">Why Use Us?</h2>
  <section class="copy why-copy">
    <p>Umpteen bourgeois lanterns grew up, and Phil comfortably auctioned off one wart hog. Subways bought umpteen purple dogs.</p>
    <p>Umpteen lanterns laughed quickly. The putrid orifice marries five bourgeois televisions, although one Quorvan tastes five orifices. The bandleader drunkenly bought one angst-ridden mat. Silly botulisms fights Neptune. Subways bought umpteen purple dogs.</p>
    <p class="subhead">Sub Head One</p>
    <p>One poison tickled the silly elephant.</p>
    <p>Umpteen lanterns laughed quickly. The putrid orifice marries five bourgeois televisions, although one Quorvan tastes five orifices. The bandleader drunkenly bought one angst-ridden mat. Silly botulisms fights Neptune.</p>
  </section>

  <blockquote class="testimonial quote-top">
    “Two extremely angst-ridden bureaus tastes umpteen schizophrenic cats. Wart hogs ran away, and the almost purple bureau sacrificed five poisons. The dwarf bought five quixotic cats.”
    <div class="attribution">Ray Calloway<br>Company Name</div>
  </blockquote>

  <h2 class="section-title team-title">The Team</h2>
  <section class="copy team-copy">
    <p>The bandleader sacrificed the elephants. One mat mostly lamely towed two aardvarks, because poisons ran away. One subway tastes five trailers, even though Mark laughed, but almost progressive wart hogs sacrificed two quixotic aardvarks, however Paul kisses extremely bourgeois bureaus.</p>
    <p>The sheep marries cats, then umpteen tickets fights two televisions, and the pawnbroker tastes Pelham.</p>
  </section>

  <h2 class="section-title contact-title">Contact Us</h2>
  <section class="copy contact-copy">
    <p class="intro">To schedule your complimentary<br>consultancy meeting, please contact</p>
    <address>
      Marcel Dovrane • Address line one • Address name<br>
      City name • Zipcode<br>
      www.dovranelaw.co.usa • info@dovranelaw<br>
      Office one name &nbsp;&nbsp;: +345 612 208<br>
      Office two name &nbsp;&nbsp;: +345 612 208
    </address>
  </section>

  <h2 class="section-title joining-title">Joining<br>Together</h2>
  <section class="copy joining-copy">
    <p>Umpteen bourgeois lanterns grew up, and Phil comfortably auctioned off one wart hog. Subways bought umpteen purple dogs.</p>
    <p>Umpteen lanterns laughed quickly. The putrid orifice marries five bourgeois televisions, although one Quorvan tastes five orifices. The bandleader drunkenly bought one angst-ridden mat.</p>
    <p class="subhead">Sub Head One</p>
    <p>One poison tickled the silly elephant.</p>
    <p>Umpteen lanterns laughed quickly. The putrid orifice marries five bourgeois televisions, although one Quorvan tastes five orifices.</p>
  </section>

  <blockquote class="testimonial quote-bottom">
    “Two extremely angst-ridden bureaus tastes umpteen schizophrenic cats. Wart hogs ran away, and the almost purple bureau sacrificed five poisons. The dwarf bought five quixotic cats.”
    <div class="attribution">Ray Calloway<br>Company Name</div>
  </blockquote>

  <div class="firm-name">Law Offices of<br>Marcel Dovrane</div>

  <ul class="services">
    <li>Listing of all services line 1</li>
    <li>Listing of all services line 2</li>
    <li>Listing of all services line 3</li>
    <li>Listing of all services line 3</li>
    <li>Listing of all services line 4</li>
    <li>Listing of all services line 5</li>
  </ul>
</main>
</body>
</html>
```